Basic loan proposal for mortgage broker needs wow factor design in Word

I have a basic word template that is quite ugly. I would like a designer to make it wow!

There are merge fields all over it and they need to be in there

My website is www.tovrenlending.com.au for logo

Home Loans

Home Loans

```html
<!DOCTYPE html>
<html lang="en">
<head>
<meta charset="utf-8">
<title>Tovren Lending – Preliminary Assessment &amp; Credit Proposal</title>
<link rel="stylesheet" href="https://fonts.googleapis.com/css2?family=Roboto:wght@300;400;500;700&display=swap">
<style>
:root{
  --backdrop:#a9a6a8;
  --navy:#18222f;
  --stripe:#9d9fa3;
  --label-bg:#e4e4e4;
  --rule:#c4c4c4;
  --ink:#3a3a3a;
  --muted:#8a8a8a;
  --paper:#ffffff;
}
*{box-sizing:border-box;margin:0;padding:0}
html,body{width:1200px;height:4178px;overflow:hidden}
body{background:var(--backdrop);font-family:"Roboto",Arial,sans-serif;color:var(--ink);position:relative}
.page{position:absolute;width:442px;height:628px;background:var(--paper);overflow:hidden}
.header{position:absolute;left:0;top:0;width:442px;height:112px}
.brand{position:absolute;top:14px;color:#fff;font-weight:400;font-size:27px;letter-spacing:-0.5px;line-height:1}
.brand small{display:block;font-size:4px;letter-spacing:0;margin-top:5px;color:#cfd3d8}
.brand.left{left:26px}
.brand.right{right:24px;text-align:left}
.page-title{position:absolute;top:56px;right:24px;font-weight:300;font-size:13px;letter-spacing:.3px;color:var(--navy)}
.content{position:absolute;left:28px;right:24px;top:84px}
.bar{background:var(--navy);color:#fff;font-weight:700;font-size:6.2px;letter-spacing:.3px;padding:2px 6px;margin:9px 0 4px;text-transform:uppercase}
.label{background:var(--label-bg);font-size:5.2px;padding:2.5px 6px;margin:5px 0 3px;text-transform:uppercase;color:#555}
.field{font-size:4.4px;color:#666;margin:3px 0 2px 2px}
.text{font-size:4.8px;line-height:1.35;margin:2px 0 3px}
.note{font-size:4.4px;line-height:1.35;margin:4px 0 3px 6px;color:#555}
.rule{border-bottom:.6px solid var(--rule);height:9px}
.footer{position:absolute;bottom:9px;font-size:5px;font-weight:700;color:#9a9a9a;letter-spacing:.2px}
.footer b{color:var(--navy)}
.footer.left{left:26px}
.footer.right{right:24px}
.kv{font-size:4.8px;margin:2px 0}
.section-title{text-align:center;font-weight:400;font-size:13px;color:var(--navy);margin:8px 0 6px;letter-spacing:.3px}
.check{display:flex;gap:8px;align-items:flex-start;margin:7px 0 0 10px;font-size:4.6px;line-height:1.35}
.check i{flex:none;width:13px;height:13px;border:.7px solid #888}
.sign{border-bottom:.6px solid #777;width:150px;margin:18px auto 0}
table.est{width:100%;border-collapse:collapse;margin-top:4px}
table.est td{border:.6px solid var(--rule);height:9px}
.cover-title{position:absolute;right:22px;top:22px;text-align:left;color:var(--navy)}
.cover-title .t1{font-weight:700;font-size:22px;line-height:1.05}
.cover-title .t2{font-weight:300;font-size:13px;color:var(--muted);margin-top:2px}
</style>
</head>
<body>

<!-- Page 1 : cover -->
<section class="page" style="left:594px;top:94px">
  <svg class="header" viewBox="0 0 442 112" aria-hidden="true">
    <polygon points="0,0 215,0 150,112 0,112" fill="var(--navy)"/>
    <polygon points="226,0 248,0 183,112 161,112" fill="var(--stripe)"/>
  </svg>
  <div class="brand left" style="top:28px">tovren<small>{organization.logo.large}</small></div>
  <div class="cover-title"><div class="t1">PRELIMINARY<br>ASSESSMENT</div><div class="t2">&amp; CREDIT PROPOSAL</div></div>
  <div class="content" style="top:128px">
    <p class="kv">Issue date: {system.currentDate}</p>
    <div class="bar">About you</div>
    <p class="field">{{brokerTextTable:borrowers}}</p>
    <div class="rule"></div><div class="rule"></div>
    <div class="bar" style="margin-top:14px">About us</div>
    <div class="label">Broker details</div>
    <p class="kv">Broker: {deal.owner.name.full}</p>
    <p class="kv">Credit Representative Name: {deal.owner.license.name}</p>
    <p class="kv">Credit Representative Number: {deal.owner.license.crn}</p>
    <p class="kv">{deal.owner.license.abn} &nbsp;&nbsp;&nbsp;&nbsp; {deal.owner.license.acn}</p>
    <p class="kv">Member Number:</p>
    <p class="kv">Business Name: {deal.owner.license.business}</p>
    <p class="kv">Address: {deal.owner.address}</p>
    <p class="kv">Phone Number: {deal.owner.phone}</p>
    <p class="kv">Email: {deal.owner.email}</p>
    <div class="label">Licensee details</div>
    <p class="kv">Australian Credit Licence Name: {organization.license.name}</p>
    <p class="kv">Australian Credit Licence Number: {organization.license.acl}</p>
    <p class="kv">Business Name: {organization.license.business}</p>
    <p class="kv">Address: {organization.license.address}</p>
    <p class="kv">Phone Number: {organization.license.phone}</p>
    <p class="kv">Email: {organization.license.email}</p>
    <p class="text" style="margin-top:5px">If your Broker is a Credit Representative, this Preliminary Assessment &amp; Credit Proposal is being provided on behalf of the Licensee.</p>
    <div class="bar">About this preliminary assessment &amp; credit proposal</div>
    <p class="text">This Preliminary Assessment &amp; Credit Proposal sets out important information that we must give you when we provide you with credit assistance.</p>
    <p class="text">This document outlines:<br>• the information provided by you in relation to your financial situation, requirements and objectives;<br>• the preliminary assessment we completed to ensure we recommended a loan which is not unsuitable for you;<br>• our recommendation and why we believe this is in your best interests;<br>• fees and charges payable; and<br>• commissions that we or other parties may receive in relation to the proposed loans.</p>
    <p class="text">Please read through and sign the Client Acknowledgement to indicate that the content is true and correct at the time of signing.</p>
  </div>
  <div class="footer right">PRELIMINARY ASSESSMENT <b>&amp; CREDIT PROPOSAL</b> &nbsp; 1</div>
</section>

<!-- Page 2 -->
<section class="page" style="left:152px;top:765px">
  <svg class="header" viewBox="0 0 442 112" aria-hidden="true">
    <polygon points="0,0 235,0 185,75 0,75" fill="var(--navy)"/>
    <polygon points="246,0 268,0 218,75 196,75" fill="var(--stripe)"/>
  </svg>
  <div class="brand left">tovren<small>{organization.logo.large}</small></div>
  <div class="page-title">PRELIMINARY ASSESSMENT</div>
  <div class="content">
    <div class="bar">Assessment details</div>
    <p class="text">We have based this assessment on the information provided by you in the Client Needs Analysis. We have assessed that this particular credit application is NOT UNSUITABLE for you. This assessment is valid for 90 days from the date it has been issued.</p>
    <div class="bar">Monthly financial position</div>
    <p class="text">A summary of your current versus proposed monthly financial position (including a buffer/floor rate) is set out below. The calculations are based on the information you provided and we verified.</p>
    <p class="field">{{brokerTextTable:MonthlyFinancialPosition:Buffer}}</p>
    <div class="rule"></div>
    <p class="note">• Buffer is calculated as: 80.00% of rental income added to gross income, 3.00% buffer on current mortgage rates, 5.25% as floor rate on proposed loan rates.</p>
    <div class="bar">Needs &amp; objectives</div>
    <div class="label">Primary reasons for seeking credit/your needs &amp; objectives</div>
    <p class="field">{{deal.objectives.needsAndObjectives.reason}}</p>
    <div class="rule"></div><div class="rule"></div><div class="rule"></div>
    <div class="label" style="margin-top:8px">Immediate needs &amp; objectives – within the next two years (e.g. holiday, purchases, renovations, savings, protect the family, etc.)</div>
    <p class="field">{{deal.objectives.needsAndObjectives.immediateTerm}}</p>
    <div class="rule"></div><div class="rule"></div><div class="rule"></div>
    <div class="label" style="margin-top:8px">Longer term – between 2 to 10 years' time (e.g. repay mortgage, buy a new car, education expenses, purchase investment property, retirement planning, etc.)</div>
    <p class="field">{{deal.objectives.needsAndObjectives.longTerm}}</p>
    <div class="rule"></div><div class="rule"></div><div class="rule"></div>
    <div class="bar" style="margin-top:10px">Requirements &amp; objectives</div>
    <p class="field">{{dealTable:loanPurpose}}</p>
    <div class="rule"></div>
    <p class="field">{{dealTable:requirementsAndObjectives}}</p>
    <div class="rule"></div><div class="rule"></div><div class="rule"></div><div class="rule"></div>
  </div>
  <div class="footer left">2 &nbsp; <b>PRELIMINARY ASSESSMENT</b> &amp; CREDIT PROPOSAL</div>
</section>

<!-- Page 3 -->
<section class="page" style="left:594px;top:765px">
  <svg class="header" viewBox="0 0 442 112" aria-hidden="true">
    <polygon points="300,0 442,0 442,75 250,75" fill="var(--navy)"/>
    <polygon points="270,0 292,0 242,75 220,75" fill="var(--stripe)"/>
  </svg>
  <div class="brand right">tovren<small>{organization.logo.large}</small></div>
  <div class="content">
    <div class="bar">Product requirements</div>
    <p class="text">This is a summary of the specific loan features you have requested. Please ensure you have read and understood the characteristics associated with each feature.</p>
    <p class="field">{{dealTable:productRequirementsSummary}}</p>
    <div class="rule"></div><div class="rule"></div><div class="rule"></div>
    <div class="bar" style="margin-top:12px">Broker disclosure</div>
    <p class="field">{{brokerTextTable:brokerDisclosure}}</p>
    <div class="rule"></div>
    <p class="note">* Please refer to the Risks/Benefits Statements which covers the risks and benefits of your requested loan features.</p>
    <div class="bar">What is most important for you?</div>
    <p class="field">{{dealTable:mostImportantForYou}}</p>
    <div class="rule"></div><div class="rule"></div><div class="rule"></div>
    <div class="bar" style="margin-top:12px">Term of credit sought</div>
    <p class="field">{{dealTable:termOfCreditSought}}</p>
    <div class="rule"></div><div class="rule"></div>
    <div class="bar" style="margin-top:12px">Broker analysis</div>
    <div class="label">Analysis, assessment and applicant education comments</div>
    <p class="field">{{notes.advice.brokerAnalysisComments}}</p>
    <div class="rule"></div><div class="rule"></div>
    <div class="bar" style="margin-top:10px">Loan products/features compared</div>
    <p class="text">Based on the information provided by you, we compared the following lenders and products before making our recommendation:</p>
    <p class="field">{{brokerTextTable:compareProductsComplex}}</p>
    <div class="rule"></div><div class="rule"></div>
    <p class="note">* Lenders Mortgage Insurance (LMI) is allocated to the primary split of the proposed loan product. This allocation may vary in accordance with your requirements and/or the lender's credit criteria.</p>
    <p class="field">{{brokerChart:compareProducts}}</p>
    <div class="rule"></div><div class="rule"></div>
    <p class="note">* The above chart shows the principal, interest and fees payable for the compared loans.</p>
  </div>
  <div class="footer right">PRELIMINARY ASSESSMENT <b>&amp; CREDIT PROPOSAL</b> &nbsp; 3</div>
</section>

<!-- Page 4 -->
<section class="page" style="left:152px;top:1433px">
  <svg class="header" viewBox="0 0 442 112" aria-hidden="true">
    <polygon points="0,0 235,0 185,75 0,75" fill="var(--navy)"/>
    <polygon points="246,0 268,0 218,75 196,75" fill="var(--stripe)"/>
  </svg>
  <div class="brand left">tovren<small>{organization.logo.large}</small></div>
  <div class="page-title" style="right:84px">CREDIT PROPOSAL</div>
  <div class="content">
    <div class="bar" style="margin-top:0">Loan products/features recommended</div>
    <p class="text">Based on your circumstances and the features relevant to your requirements and objectives, we recommend the following lender and product:</p>
    <p class="field">{{brokerTextTable:recommendedProduct}}</p>
    <div class="rule"></div><div class="rule"></div>
    <p class="note">* Interest rates, fees and repayments may change if the lender changes its loan terms.</p>
    <p class="field">{{brokerTextChart:repayments}}</p>
    <div class="rule"></div><div class="rule"></div>
    <p class="note">* If an offset account is available for your recommended loan/s, the above graph compares a loan operating without an offset account against a loan linked with an offset account. This calculation is based on your initial offset balance and estimated monthly offer contribution.</p>
    <div class="label">Product suitability</div>
    <p class="field">{{brokerTextProductSuitability}} &nbsp; {{brokerTextProductSuitabilityReasons}}</p>
    <div class="rule"></div><div class="rule"></div><div class="rule"></div><div class="rule"></div>
    <div class="bar" style="margin-top:10px">Why our recommendation meets your best interests</div>
    <div class="label">Options presented and recommendation comments</div>
    <p class="field">{{notes.advice.optionsAndRecommendation}}</p>
    <div class="rule"></div>
    <div class="label" style="margin-top:7px">Explanation for selecting interest only repayment (if applicable)</div>
    <p class="field">{{notes.advice.interestOnlyReason}}</p>
    <div class="rule"></div>
    <div class="label" style="margin-top:7px">Explanation for selecting fixed rate product (if applicable)</div>
    <p class="field">{{notes.advice.fixedRateReason}}</p>
    <div class="rule"></div>
    <div class="label" style="margin-top:7px">Line of credit comments (if applicable)</div>
    <p class="field">{{notes.advice.lineOfCredit}}</p>
    <div class="rule"></div>
    <div class="label" style="margin-top:7px">Interest in advance comments (if applicable)</div>
    <p class="field">{{notes.advice.interestInAdvance}}</p>
    <div class="rule"></div>
  </div>
  <div class="footer left">4 &nbsp; <b>PRELIMINARY ASSESSMENT</b> &amp; CREDIT PROPOSAL</div>
</section>

<!-- Page 5 -->
<section class="page" style="left:594px;top:1433px">
  <svg class="header" viewBox="0 0 442 112" aria-hidden="true">
    <polygon points="300,0 442,0 442,75 250,75" fill="var(--navy)"/>
    <polygon points="270,0 292,0 242,75 220,75" fill="var(--stripe)"/>
  </svg>
  <div class="brand right">tovren<small>{organization.logo.large}</small></div>
  <div class="content">
    <div class="label" style="margin-top:0">Conflict of interest disclosure</div>
    <p class="field">{{dealFinancialTable:conflictOfInterest}}</p>
    <div class="rule"></div>
    <div class="label" style="margin-top:8px">Security to be provided by you</div>
    <p class="field">{{brokerTextTable:securityDetails}}</p>
    <div class="rule"></div>
    <div class="label" style="margin-top:8px">Funding worksheet</div>
    <p class="field">{{brokerTextTable:fundingWorksheet}}</p>
    <div class="rule"></div><div class="rule"></div>
    <p class="note">* If you are refinancing, please refer to the Refinance Analysis which considers the costs of a refinance with the benefits you could receive from your proposed loan/s.</p>
    <div class="bar">Estimated fees &amp; charges payable by you for your loan/s</div>
    <p class="text">An estimate of the total fees and charges that may be payable by you to the lender in relation to applying for the loan/s are listed in the table below:</p>
    <p class="field">{{brokerTextTable:fundsApplied}}</p>
    <div class="rule"></div><div class="rule"></div>
    <p class="note">* These fees and charges are one-off payments unless otherwise indicated. These amounts are estimates only and the final figures will be shown in the credit contract issued by the lender. Some or all of these fees and charges may be payable from the loan proceeds.</p>
    <div class="bar">Estimated fees payable by you to us</div>
    <p class="text">If a fee is payable by you, this will have been disclosed in the Credit Guide we have previously given to you. The Credit Quote will outline any fees payable for providing credit assistance and the time that they are payable. If you did not receive a Credit Quote, this will indicate that no fees are payable.</p>
    <div class="bar">How are we paid?</div>
    <p class="text">We are remunerated by commission from your recommended lender and this is generally by way of both an upfront and trail commission based on your loan amount.</p>
    <p class="text">Upfront commission is a one-off commission paid after settlement with a maximum upfront commission of 1.5%.</p>
    <p class="text">Trail commission is an ongoing commission paid generally over the life of the loan and is based on the monthly balance of your loan amount. This commission is a maximum of 0.5% per annum.</p>
    <p class="text">Commissions are paid based on a percentage of the loan drawn down in most cases net of any offset amount. The way commissions are calculated and paid to us by lenders may vary. By following the responsible lending and best interests obligations, we will ensure that the loan/s recommended to you is not unsuitable to your requirements and objectives.</p>
    <p class="text">These commissions may be shared between {organization.license.institution1}, the Broker and any referring party (as disclosed in this Preliminary Assessment &amp; Credit Proposal).</p>
    <p class="text">We are not eligible for volume bonuses in relation to the loan/s.</p>
  </div>
  <div class="footer right">PRELIMINARY ASSESSMENT <b>&amp; CREDIT PROPOSAL</b> &nbsp; 5</div>
</section>

<!-- Page 6 -->
<section class="page" style="left:152px;top:2103px">
  <svg class="header" viewBox="0 0 442 112" aria-hidden="true">
    <polygon points="0,0 235,0 185,75 0,75" fill="var(--navy)"/>
    <polygon points="246,0 268,0 218,75 196,75" fill="var(--stripe)"/>
  </svg>
  <div class="brand left">tovren<small>{organization.logo.large}</small></div>
  <div class="content">
    <div class="bar" style="margin-top:0">Other fees/benefits we may be entitled to be paid</div>
    <p class="text">Other benefits may be received from our panel of lenders from time to time. These benefits may include benefits such as attendance at social events, higher servicing standards from lenders and training and educational opportunities.</p>
    <p class="text">You are entitled to ask your Broker if any additional fees or benefits may be applicable to your credit application.</p>
    <div class="bar">Reasonable estimate of commission</div>
    <p class="text">An estimate of commission to be received by the Licensee from the lender for assisting you to obtain the finance are listed in the table below.</p>
    <p class="text">We may receive an upfront commission, payable shortly after settlement.</p>
    <p class="text">We also receive a monthly commission calculated as the percentage of the outstanding loan balance. Details of these commissions are listed in the table below.</p>
    <p class="text">An estimate of referral fees payable by us to any third parties are also listed in the table below.</p>
    <table class="est"><tr><td></td><td></td><td></td><td></td></tr><tr><td></td><td></td><td></td><td></td></tr><tr><td></td><td></td><td></td><td></td></tr><tr><td></td><td></td><td></td><td></td></tr></table>
    <div class="bar" style="margin-top:14px">Additional commentary relevant to your circumstances</div>
    <div class="label">Borrowing power commentary</div>
    <p class="field">{{notes.advice.comments.borrowingPower}}</p>
    <div class="rule"></div><div class="rule"></div>
    <div class="label" style="margin-top:8px">Deposit/equity comments</div>
    <p class="field">{{notes.advice.comments.depositEquity}}</p>
    <div class="rule"></div><div class="rule"></div>
    <div class="label" style="margin-top:8px">Credit history comments</div>
    <p class="field">{{notes.advice.comments.creditHistory}}</p>
    <div class="rule"></div><div class="rule"></div>
    <div class="label" style="margin-top:8px">Security (property) notes</div>
    <p class="field">{{notes.advice.comments.security}}</p>
    <div class="rule"></div><div class="rule"></div>
    <div class="label" style="margin-top:8px">Living expenses comments</div>
    <p class="field">{{notes.advice.comments.livingExpenses}}</p>
    <div class="rule"></div>
  </div>
  <div class="footer left">6 &nbsp; <b>PRELIMINARY ASSESSMENT</b> &amp; CREDIT PROPOSAL</div>
</section>

<!-- Page 7 -->
<section class="page" style="left:594px;top:2103px">
  <svg class="header" viewBox="0 0 442 112" aria-hidden="true">
    <polygon points="300,0 442,0 442,75 250,75" fill="var(--navy)"/>
    <polygon points="270,0 292,0 242,75 220,75" fill="var(--stripe)"/>
  </svg>
  <div class="brand right">tovren<small>{organization.logo.large}</small></div>
  <div class="content">
    <h2 class="section-title">INSURANCE DECLARATION</h2>
    <p class="text">To ensure we have taken the appropriate duty of care when arranging finance on your behalf, we must make you aware of the need to protect yourself, your family and your business from the possible financial hardship caused by death, disability, trauma or personal injury.</p>
    <p class="text">If you do not have adequate risk insurance in place, you may not be able to make the repayments on your loan/s if you had an accident or illness that stopped you working, or in the event of permanent disability or death. It is important that you understand the risks of not maintaining sufficient insurance to protect your loan/s and your assets.</p>
    <div class="check"><i></i><span>I/We acknowledge that my/our Broker has brought this to our attention</span></div>
    <div class="check"><i></i><span>I/We understand that insurance is not compulsory and is not a condition of the loan/s being approved</span></div>
    <div class="check"><i></i><span>I/We have considered the risks and are satisfied with the current level of personal insurance protection or have made my/our own arrangements</span></div>
    <p class="text" style="margin:4px 0 0 31px">OR</p>
    <div class="check" style="margin-top:3px"><i></i><span>I/We have considered the risks and would like to discuss the insurance options with someone recommended by my/our Broker</span></div>
    <div class="sign" style="margin-top:30px"></div>
    <h2 class="section-title" style="margin-top:26px">CLIENT ACKNOWLEDGEMENT</h2>
    <p class="text">By signing this Preliminary Assessment &amp; Credit Proposal, you agree and acknowledge that this assessment is based on the requirements and objectives, income and expenses which you have provided to {organization.license.institution1}.</p>
    <p class="text">You should check carefully that the information provided in this document (and its appendices) is accurate and up-to-date and that there is no omissions or inaccuracies (including any foreseeable changes to your financial situation) which may impact on your ability to meet the payment requirements in the credit contract for which you have applied.</p>
    <p class="field" style="margin-top:14px">{{dealTable:signatures}}</p>
    <div class="rule" style="margin-left:110px"></div>
    <div class="rule" style="margin-left:110px;height:22px"></div>
    <div class="rule" style="margin-left:110px;height:22px"></div>
  </div>
  <div class="footer right">PRELIMINARY ASSESSMENT <b>&amp; CREDIT PROPOSAL</b> &nbsp; 7</div>
</section>

<!-- Page 8 -->
<section class="page" style="left:152px;top:2773px">
  <svg class="header" viewBox="0 0 442 112" aria-hidden="true">
    <polygon points="0,0 235,0 185,75 0,75" fill="var(--navy)"/>
    <polygon points="246,0 268,0 218,75 196,75" fill="var(--stripe)"/>
  </svg>
  <div class="brand left">tovren<small>{organization.logo.large}</small></div>
  <div class="content">
    <h2 class="section-title" style="margin-top:0">APPENDIX 1:</h2>
    <div class="bar">Risk/benefits statements</div>
    <p class="field">{{brokerTextDocumentsBenefits}}</p>
    <div class="rule"></div>
    <h2 class="section-title" style="margin-top:14px">APPENDIX 2:</h2>
    <div class="bar">Refinance analysis</div>
    <p class="field">{{brokerTextTableRefinanceAnalysis}}</p>
    <p class="field">{{brokerTextTableRefinanceAnalysisBenefits}}</p>
    <p class="field">{{brokerTextTableRefinanceAnalysisAdvancedMonthlyRepayments}}</p>
    <p class="field">{{brokerTextTableRefinanceAnalysisReasons}}</p>
    <p class="note">* If you are not refinancing, this Refinance Analysis has been intentionally left blank.</p>
    <h2 class="section-title" style="margin-top:14px">APPENDIX 3:</h2>
    <div class="bar">Client needs analysis</div>
    <div class="label">Personal details</div>
    <p class="field">{{contactTableContact1GeneralDetails}}</p>
    <p class="field">{{contactTableContact1ContactDetails}}</p>
    <p class="field">{{contactTableContact1AddressDetails}}</p>
    <p class="field">{{contactTableContact1IdentificationDetails}}</p>
    <p class="field">{{contactTableContact1FamilyRelations}}</p>
    <p class="field">{{contactTableContact1NextOfKin}}</p>
    <p class="field">{{contactTableContact2GeneralDetails}}</p>
    <p class="field">{{contactTableContact2ContactDetails}}</p>
    <p class="field">{{contactTableContact2AddressDetails}}</p>
    <p class="field">{{contactTableContact2FamilyRelations}}</p>
    <p class="field">{{contactTableContact2NextOfKin}}</p>
    <p class="field">{{contactTableContact3GeneralDetails}}</p>
    <p class="field">{{contactTableContact3ContactDetails}}</p>
    <p class="field">{{contactTableContact3AddressDetails}}</p>
  </div>
  <div class="footer left">8 &nbsp; <b>PRELIMINARY ASSESSMENT</b> &amp; CREDIT PROPOSAL</div>
</section>

<!-- Page 9 -->
<section class="page" style="left:594px;top:2773px">
  <svg class="header" viewBox="0 0 442 112" aria-hidden="true">
    <polygon points="300,0 442,0 442,75 250,75" fill="var(--navy)"/>
    <polygon points="270,0 292,0 242,75 220,75" fill="var(--stripe)"/>
  </svg>
  <div class="brand right">tovren<small>{organization.logo.large}</small></div>
  <div class="content" style="top:30px;right:160px">
    <p class="field">{{contactTableContact3IdentificationDetails}}</p>
    <p class="field">{{contactTableContact3FamilyRelations}}</p>
    <p class="field">{{contactTableContact3NextOfKin}}</p>
    <p class="field">{{contactTableContact4GeneralDetails}}</p>
    <p class="field">{{contactTableContact4ContactDetails}}</p>
    <p class="field">{{contactTableContact4AddressDetails}}</p>
    <p class="field">{{contactTableContact4IdentificationDetails}}</p>
    <p class="field">{{contactTableContact4FamilyRelations}}</p>
    <p class="field">{{contactTableContact4NextOfKin}}</p>
  </div>
  <div class="content" style="top:128px">
    <div class="label">Income</div>
    <p class="field">{{contactTableAnnualIncomeSummary}}</p>
    <div class="rule"></div><div class="rule"></div>
    <div class="label" style="margin-top:10px">Expenses</div>
    <p class="field">{{dealTableExpensesByHouseholdWithComments}}</p>
    <div class="rule"></div><div class="rule"></div>
    <div class="label" style="margin-top:10px">Assets</div>
    <p class="field">{{dealTableAssets}}</p>
    <div class="rule"></div><div class="rule"></div>
    <div class="label" style="margin-top:10px">Liabilities</div>
    <p class="field">{{dealTableLiabilitiesExtended}}</p>
    <div class="rule"></div>
    <p class="note">* The credit card monthly repayment is calculated at a rate of 3.8% of the credit card limit.</p>
    <div class="label">Insurers</div>
    <p class="field">{{dealTableInsuranceProviders}}</p>
    <div class="rule"></div><div class="rule"></div>
    <div class="label" style="margin-top:10px">Other advisers</div>
    <p class="field">{{dealTableOtherAdvisers}}</p>
    <div class="rule"></div>
  </div>
  <div class="footer right">PRELIMINARY ASSESSMENT <b>&amp; CREDIT PROPOSAL</b> &nbsp; 9</div>
</section>

<!-- Page 10 -->
<section class="page" style="left:152px;top:3438px">
  <svg class="header" viewBox="0 0 442 112" aria-hidden="true">
    <polygon points="0,0 235,0 185,75 0,75" fill="var(--navy)"/>
    <polygon points="246,0 268,0 218,75 196,75" fill="var(--stripe)"/>
  </svg>
  <div class="brand left">tovren<small>{organization.logo.large}</small></div>
  <div class="content">
    <div class="label" style="margin-top:0">Possible changes to financial situation</div>
    <p class="field">{{dealTableAdverseChangesInFinancialSituation}}</p>
    <div class="rule"></div><div class="rule"></div><div class="rule"></div>
    <p class="field" style="margin-top:8px">{{dealTableBeneficialChangesInFinancialSituation}}</p>
    <div class="rule"></div><div class="rule"></div><div class="rule"></div>
    <div class="label" style="margin-top:12px">Exit strategy</div>
    <p class="field">{{dealTableExitStrategy}}</p>
    <div class="rule"></div><div class="rule"></div><div class="rule"></div>
    <div class="label" style="margin-top:12px">Your financial security</div>
    <p class="field">{{dealTableYourFinancialSecurityView}}</p>
    <div class="rule"></div><div class="rule"></div><div class="rule"></div>
    <div class="label" style="margin-top:12px">Your credit history</div>
    <p class="field">{{dealTableYourCreditHistoryView}}</p>
    <div class="rule"></div><div class="rule"></div><div class="rule"></div>
    <div class="label" style="margin-top:12px">Verifications completed</div>
    <p class="field">{{brokerTextTableInterviewDetails}}</p>
    <div class="rule"></div><div class="rule"></div>
    <p class="field" style="margin-top:6px">{{brokerTextTableVerificationsCompleted}}</p>
    <div class="rule"></div><div class="rule"></div><div class="rule"></div>
  </div>
  <div class="footer left">10 &nbsp; <b>PRELIMINARY ASSESSMENT</b> &amp; CREDIT PROPOSAL</div>
</section>

</body>
</html>
```